Buch-/eBook-Cover für Frauen zwischen 16-35
Zielgruppe
MLT/ Mellow Lantern Typesetting. Ich suche Unterstützung für die Erstellung eines Buchcovers für Frauen zwischen 16-35.
Aufgabenstellung
Ich habe eine Zusammenfassung des Projektes in dem beigefügten Word Dokument zusammen mit Beispielcovern, Covern der Konkurrenz etc.

```html
<!DOCTYPE html>
<html lang="de">
<head>
<meta charset="utf-8">
<title>Das große Mutproben-Buch für beste Freundinnen – Cover</title>
<link rel="stylesheet" href="https://fonts.googleapis.com/css2?family=Gochi+Hand&family=Poppins:wght@300;400&display=swap">
<style>
  :root {
    --page-bg: #fbeee4;
    --cover-cream: #faf4e6;
    --cover-cream-deep: #f3e6cc;
    --ink-navy: #2c3a4d;
    --accent-red: #d8503c;
    --accent-orange: #e0663f;
    --box-pink: #fbd8d0;
    --leaf-teal: #3f7f8a;
    --leaf-orange: #e59a6a;
    --figure-blue: #3d5f7d;
    --figure-yellow: #e9b640;
  }
  * { margin: 0; padding: 0; box-sizing: border-box; }
  html, body { width: 1200px; height: 1200px; overflow: hidden; }
  body {
    background: var(--page-bg);
    display: flex;
    align-items: center;
    justify-content: center;
    gap: 44px;
  }
  .cover {
    width: 520px;
    height: 780px;
    position: relative;
    background: linear-gradient(180deg, var(--cover-cream) 0%, var(--cover-cream-deep) 100%);
    box-shadow: 0 8px 30px rgba(140, 80, 50, 0.18);
    overflow: hidden;
  }
  .leaf-band {
    position: absolute;
    left: 0; right: 0;
    background: linear-gradient(90deg, rgba(63,127,138,0.3), rgba(229,154,106,0.35), rgba(63,127,138,0.3));
  }
  .leaf-band.top { top: 0; height: 96px; }
  .leaf-band.bottom { bottom: 0; height: 130px; }
  .leaf-side {
    position: absolute;
    width: 80px;
    height: 240px;
    bottom: 30px;
    background: linear-gradient(180deg, rgba(63,127,138,0), rgba(229,154,106,0.35));
  }
  .leaf-side.left { left: 0; }
  .leaf-side.right { right: 0; }

  .front-title {
    position: absolute;
    top: 122px;
    left: 20px; right: 20px;
    text-align: center;
    font-family: "Gochi Hand", cursive;
    font-size: 46px;
    line-height: 1.08;
    color: var(--ink-navy);
    text-transform: uppercase;
    letter-spacing: 1px;
  }
  .front-subtitle {
    position: absolute;
    top: 372px;
    left: 100px; right: 100px;
    background: var(--box-pink);
    border-radius: 14px;
    padding: 12px 16px;
    text-align: center;
    font-family: "Gochi Hand", cursive;
    font-size: 20px;
    line-height: 1.3;
    color: var(--accent-red);
    text-transform: uppercase;
    letter-spacing: 1px;
  }
  .friends-illustration {
    position: absolute;
    left: 130px;
    bottom: 0;
    width: 260px;
    height: 240px;
    border-radius: 110px 110px 0 0;
    background: linear-gradient(90deg, var(--figure-blue) 0%, var(--figure-blue) 46%, var(--figure-yellow) 54%, var(--figure-yellow) 100%);
    opacity: 0.85;
  }

  .back-headline {
    position: absolute;
    top: 44px;
    left: 30px; right: 30px;
    text-align: center;
    font-family: "Gochi Hand", cursive;
    font-size: 28px;
    line-height: 1.18;
    color: var(--accent-orange);
    text-transform: uppercase;
  }
  .back-blurb {
    position: absolute;
    top: 170px;
    left: 40px; right: 40px;
    background: var(--box-pink);
    border-radius: 16px;
    padding: 24px 26px;
    font-family: "Poppins", sans-serif;
    font-weight: 300;
    font-size: 15px;
    line-height: 1.55;
    color: var(--accent-red);
    text-align: center;
  }
  .back-blurb p + p { margin-top: 16px; }
</style>
</head>
<body>
  <section class="cover cover-front">
    <div class="leaf-band top" role="img" aria-label="Ranken aus Blättern und Beeren in Petrol und Orange"></div>
    <div class="leaf-side left" role="img" aria-label="Blattranken am linken Rand"></div>
    <div class="leaf-side right" role="img" aria-label="Blattranken am rechten Rand"></div>
    <h1 class="front-title">Das große<br>Mutproben-<br>Buch für<br>beste Freundinnen</h1>
    <p class="front-subtitle">Zusammen wachsen,<br>lachen und die Welt<br>entdecken</p>
    <div class="friends-illustration" role="img" aria-label="Illustration zweier Freundinnen von hinten, eine in Blau, eine in Gelb"></div>
  </section>

  <section class="cover cover-back">
    <h2 class="back-headline">Von Alltag zu Abenteuer:<br>Entdeckt die Magie<br>gemeinsamer Erlebnisse</h2>
    <div class="back-blurb">
      <p>Das Mutproben-Buch für beste Freundinnen bietet euch 52 abwechslungsreiche Aktivitäten, die euch ein Jahr voller Spaß, Abenteuer und unvergesslicher Erinnerungen bescheren. Ein Jahr, das eure Freundschaft für immer stärken wird.</p>
      <p>Von spannenden Outdoor-Abenteuern bis hin zu kreativen DIY-Projekten – jede Woche bringt die perfekte Aktivität und die nötige Abwechslung in euren Alltag. Stärkt eure Freundschaft, lacht gemeinsam und genießt die kostbare Zeit miteinander.</p>
      <p>Entdeckt, wie viel Freude und Abwechslung das Leben bietet, wenn ihr es zusammen erlebt. Macht jede Woche zu etwas Besonderem – mit dem Mutproben-Buch für beste Freundinnen!</p>
    </div>
    <div class="leaf-band bottom" role="img" aria-label="Ranken aus Blättern und Beeren in Petrol und Orange"></div>
  </section>
</body>
</html>
```